Small consulting business needs a website designed to highlight value and four offerings

My company is a dynamic consulting firm with four Core Offerings: Learning & Evaluation, Program Management, Facilitation & Coaching; Implementation & Transformation. Our mission is to facilitate organizational change and transformation, and to make space for creativity, joy, belonging, and trust. If done successfully, we grow to better understand ourselves, each other, and the work we do together.

I'd like the website to give a feeling of confidence and clarity. I want the colors to match or compliment my logo. I want to have three tabs - Our Clients, Our Services, and Government.

See attached Word document for additional content. My current website is www.BrightHarborGroup.com.

Some websites I'm inspired by:
https://www.quillmeadowworks.com
https://www.verolandpartners.com
https://tqvb.org

Some websites of people/groups in my field that I find uninspiring:
http://denisehollick.com
https://www.marrowfen.org

Target Market(s)

State and local government agencies, health tech, and corporate HR departments

Industry/Entity Type

public health, aging, government, health tech

Coding

Coded - Design and coding required

Number of Pages Required

4 page

Font styles to use
Other font styles liked:
• Calibri and Merriweather

Colors
0054AA
0677BA
7BADD7
CADEEF
E8F1F8
00AB8E
00BBA5
67D7C9
C6EFE9
E9F9F6
FFC000
F8CF3A
FAE287
FDF2CF
FEFAEE
F0912C
F2A743
F7CA91
FBE8D2
FDF5EE

Requirements
Must have
• Attached logo and content, water colors few, and photos.
Nice to have
• Real pictures, which I can provide to the chosen designer
Should not have
• AI generated characters or cartoons.

```html
<!DOCTYPE html>
<html lang="en">
<head>
<meta charset="utf-8">
<title>Bright Harbor Group</title>
<link rel="stylesheet" href="https://fonts.googleapis.com/css2?family=Merriweather:wght@400;700&family=Carlito:wght@400;700&family=Roboto:wght@400&display=swap">
<style>
:root{
  --ink:#1f1f1f;
  --text:#2a2a2a;
  --accent:#f0912c;
  --wash-yellow:#eef0c4;
  --wash-yellow-soft:#f6f6df;
  --wash-gold:#e7a73a;
  --wash-orange:#d9692a;
  --wash-rust:#c85220;
  --teal:#1f6f6a;
  --teal-soft:#7fb8a8;
  --gold:#f2b631;
  --olive:#b6bf4a;
  --footer:#27362a;
  --white:#ffffff;
}
*{margin:0;padding:0;box-sizing:border-box}
html,body{width:1200px;height:3630px;overflow:hidden;background:var(--white)}
body{position:relative;font-family:'Carlito',sans-serif;color:var(--text)}
.abs{position:absolute}
.serif{font-family:'Merriweather',serif}
.center{text-align:center}

/* washes */
.wash-hero{left:0;top:0;width:1200px;height:900px;
  background:radial-gradient(ellipse 62% 58% at 50% 40%,var(--wash-yellow-soft) 0%,var(--wash-yellow) 55%,rgba(238,240,196,0) 100%)}
.wash-value{left:0;top:1200px;width:1200px;height:420px;
  background:radial-gradient(ellipse 55% 60% at 50% 60%,var(--wash-yellow-soft) 0%,var(--wash-yellow) 60%,rgba(238,240,196,0) 100%)}
.wash-band{left:0;top:1470px;width:1200px;height:710px;
  background:linear-gradient(90deg,var(--wash-gold) 0%,#eaa050 28%,#e08a55 55%,var(--wash-orange) 78%,var(--wash-rust) 100%);
  -webkit-mask:radial-gradient(ellipse 80% 48% at 50% 50%,#000 70%,transparent 100%);
  mask:radial-gradient(ellipse 80% 48% at 50% 50%,#000 70%,transparent 100%)}
.wash-why{left:60px;top:2150px;width:1100px;height:560px;
  background:radial-gradient(ellipse 55% 50% at 50% 50%,var(--wash-yellow-soft) 0%,var(--wash-yellow) 60%,rgba(238,240,196,0) 100%)}

/* nav */
.brand{left:131px;top:30px;width:160px}
.brand-dot{width:44px;height:44px;border-radius:50%;background:var(--gold);margin:0 auto 14px}
.brand-name{font-family:'Merriweather',serif;font-size:19px;line-height:26px;color:var(--ink);text-align:center}
.nav{left:458px;top:75px;display:flex;gap:0;font-size:17px;color:var(--ink)}
.nav a{position:absolute;white-space:nowrap;text-decoration:none;color:var(--ink)}
.nav a.active{color:var(--accent)}

.hero-title{left:0;width:1200px;top:204px;font-size:38px;line-height:44px;font-weight:700;color:var(--ink)}
.hero-sub{left:230px;width:740px;top:298px;font-size:14px;line-height:24px;color:var(--ink)}
.puzzle{left:443px;top:373px;width:310px;height:310px;border-radius:50%;
  background:conic-gradient(from 0deg,var(--teal-soft) 0 25%,#5f9c84 25% 50%,var(--gold) 50% 75%,var(--olive) 75% 100%);
  border:6px solid var(--teal)}
.offer{font-family:'Merriweather',serif;font-size:21px;line-height:28px;color:#2b2b2b}
.offer.right{text-align:right}
.hero-tag{left:0;width:1200px;top:704px;font-size:24px;font-weight:700;color:var(--ink)}
.hero-arrow{left:588px;top:778px}

.help-kicker{left:0;width:1200px;top:946px;font-size:20px;font-weight:700;color:var(--ink)}
.help-big{left:0;width:1200px;top:990px;font-size:70px;line-height:72px;color:var(--ink)}
.chev{width:22px;height:28px}

.value-title{left:0;width:1200px;top:1356px;font-size:38px;font-weight:700;color:var(--ink)}
.value-copy{left:226px;width:748px;top:1420px;font-family:'Roboto',sans-serif;font-size:15.5px;line-height:24px;color:var(--ink)}

.collab-title{left:0;width:1200px;top:1744px;font-size:38px;font-weight:700;color:var(--white)}
.collab-item{width:200px;font-family:'Roboto',sans-serif;font-size:19.5px;line-height:28px;color:var(--white)}
.collab-item svg{display:block;margin-bottom:8px}

.burst{left:164px;top:2182px;width:410px;height:410px;border-radius:50%;
  background:radial-gradient(circle,#fdf2cf 0 22%,var(--gold) 38%,#4f9a86 62%,rgba(31,111,106,0) 72%)}
.why-title{left:625px;top:2210px;font-size:38px;font-weight:700;color:var(--ink)}
.why-copy{left:625px;width:440px;top:2272px;font-size:14.5px;line-height:24px;color:var(--text)}

.mission-title{left:162px;width:400px;top:2774px;font-size:38px;font-weight:700;color:var(--ink)}
.mission-copy{left:172px;width:380px;top:2836px;font-size:19px;line-height:28px;color:var(--text)}
.circles{left:669px;top:2738px;width:324px;height:324px;border-radius:50%;
  background:radial-gradient(circle at 45% 50%,#e9d36a 0 25%,#8fb6a0 45%,#2f6f7a 68%,rgba(47,111,122,0) 72%)}

.vision-art{left:170px;top:3092px;width:420px;height:420px;border-radius:50%;
  background:radial-gradient(circle at 50% 35%,#f5c65a 0 35%,#8fbaa2 60%,rgba(31,111,106,0) 72%)}
.vision-title{left:632px;width:400px;top:3208px;font-size:38px;font-weight:700;color:var(--ink)}
.vision-copy{left:652px;width:360px;top:3270px;font-size:19px;line-height:28px;color:var(--text)}

.footer{left:0;top:3542px;width:1200px;height:88px;background:var(--footer);
  color:var(--white);font-size:19px;display:flex;align-items:center;justify-content:center}
</style>
</head>
<body>

<div class="abs wash-hero"></div>
<div class="abs wash-value"></div>
<div class="abs wash-band"></div>
<div class="abs wash-why"></div>

<header>
  <div class="abs brand">
    <div class="brand-dot"></div>
    <div class="brand-name">Bright Harbor<br>Group</div>
  </div>
  <nav class="abs nav">
    <a class="active" href="#" style="left:0">Home</a>
    <a href="#" style="left:77px">About</a>
    <a href="#" style="left:157px">Our Clients</a>
    <a href="#" style="left:273px">Our Services</a>
    <a href="#" style="left:399px">Government</a>
    <a href="#" style="left:526px">Contact</a>
  </nav>
</header>

<section class="hero">
  <h1 class="abs hero-title serif center">A Seat at the Table for Collaboration,<br>Learning, and Meaningful Change.</h1>
  <p class="abs hero-sub center">Bright Harbor Group is a dynamic consulting firm with four Core Offerings: Learning &amp; Evaluation, Program Management, Facilitation &amp; Coaching; Implementation &amp; Transformation</p>
  <div class="abs puzzle" role="img" aria-label="Watercolor puzzle circle of four interlocking pieces in teal, green, gold and olive"></div>
  <div class="abs offer right" style="left:200px;width:210px;top:410px">Learning</div>
  <div class="abs offer" style="left:797px;top:410px">Program<br>Management</div>
  <div class="abs offer right" style="left:200px;width:210px;top:607px">Implementation</div>
  <div class="abs offer" style="left:797px;top:604px">Facilitation</div>
  <p class="abs hero-tag serif center">Here for you and your team.</p>
  <svg class="abs hero-arrow" width="24" height="46" viewBox="0 0 24 46"><path d="M12 1V44M2 33L12 44L22 33" fill="none" stroke="#1f1f1f" stroke-width="2.5"/></svg>
</section>

<section class="help">
  <p class="abs help-kicker serif center">We Help Your Team</p>
  <h2 class="abs help-big serif center" style="font-weight:400">Turn bold visions into<br>practical results.</h2>
  <svg class="abs chev" style="left:62px;top:1014px" viewBox="0 0 22 28"><path d="M15 3L5 14L15 25" fill="none" stroke="#1f1f1f" stroke-width="2.5"/></svg>
  <svg class="abs chev" style="left:1118px;top:1014px" viewBox="0 0 22 28"><path d="M7 3L17 14L7 25" fill="none" stroke="#1f1f1f" stroke-width="2.5"/></svg>
</section>

<section class="value">
  <h2 class="abs value-title serif center">Our Value</h2>
  <p class="abs value-copy center">We are the tranquility in chaos. The steady partner always at the table with you. We drive meaningful and measurable change, resulting in sustained progress towards key community outcomes and multi-sector initiatives. Our work produces values realignment, critical technical assistance, and develops strategic plans for innovative organizations ready to elevate their work.</p>
</section>

<section class="collab">
  <h2 class="abs collab-title serif center">We Collaborate With</h2>
  <svg class="abs chev" style="left:62px;top:1902px" viewBox="0 0 22 28"><path d="M15 3L5 14L15 25" fill="none" stroke="#fff" stroke-width="2.5"/></svg>
  <svg class="abs chev" style="left:1118px;top:1902px" viewBox="0 0 22 28"><path d="M7 3L17 14L7 25" fill="none" stroke="#fff" stroke-width="2.5"/></svg>
  <div class="abs collab-item" style="left:144px;top:1844px"><svg width="44" height="34" viewBox="0 0 44 34"><path d="M3 18L15 30L41 3" fill="none" stroke="#fff" stroke-width="6"/></svg>Large-scale<br>Companies</div>
  <div class="abs collab-item" style="left:410px;top:1844px"><svg width="44" height="34" viewBox="0 0 44 34"><path d="M3 18L15 30L41 3" fill="none" stroke="#fff" stroke-width="6"/></svg>National and local<br>nonprofits</div>
  <div class="abs collab-item" style="left:676px;top:1844px"><svg width="44" height="34" viewBox="0 0 44 34"><path d="M3 18L15 30L41 3" fill="none" stroke="#fff" stroke-width="6"/></svg>State government<br>agencies</div>
  <div class="abs collab-item" style="left:942px;top:1844px"><svg width="44" height="34" viewBox="0 0 44 34"><path d="M3 18L15 30L41 3" fill="none" stroke="#fff" stroke-width="6"/></svg>International<br>Partnerships &amp;<br>Organizations</div>
</section>

<section class="why">
  <div class="abs burst" role="img" aria-label="Watercolor burst of gold, teal and green strokes radiating from a center"></div>
  <h2 class="abs why-title serif">Why Us</h2>
  <p class="abs why-copy">Through our Core Offerings and guided by our founder's traditional and nontraditional methods for engaging and steering a team, we create a sense of belonging, foster transparency, and help to build stronger relationships. Our approach helps to drive meaningful change so that organizations and initiatives can clear roadblocks and meet collective goals. Our team's proven ability to transform conflict into opportunity will help to advance your organization and the communities you serve.</p>
</section>

<section class="mission">
  <h2 class="abs mission-title serif center">Our Mission</h2>
  <p class="abs mission-copy center">Our mission is to facilitate organizational change and transformation, and to make space for creativity, joy, belonging, and trust. If done successfully, we grow to better understand ourselves, each other, and the work we do together.</p>
  <div class="abs circles" role="img" aria-label="Watercolor of overlapping gold rings over teal and yellow washes"></div>
</section>

<section class="vision">
  <div class="abs vision-art" role="img" aria-label="Watercolor of a golden path leading toward a rising sun framed by leafy branches"></div>
  <h2 class="abs vision-title serif center">Our Vision</h2>
  <p class="abs vision-copy center">Our vision is to be part of a world where organizations and collaborators connect as human beings first. We envision a future where partners and colleagues strive for ongoing growth together.</p>
</section>

<footer class="abs footer">© Copyrights 2025 | All Rights Reserved</footer>

</body>
</html>
```